Infographic for explaining evidence based medicine

I need 2 diagrams for a talking I am doing later this week . The purpose of the talk is to explain the current approach to evidence based medicine and then the approach of utilising big data. The talk is to doctors who are considered experts in their field. I have attached the layout of the diagrams. Everything on them in italics is just notes. I am really just looking to stylise the people, add in some colours and make it look better than mine. There will be minimal changes.

Target Market(s)

Doctors - considered experts in their field

Industry/Entity Type

Medical And Science

Font styles to use
Serif
Sans Serif

Requirements
Must have
• Quick turn around. Simple design. Needs to make my pictures look better then I have done them.
• Need the colours as described - basicially red, orange and green people

```html
<!DOCTYPE html>
<html lang="en">
<head>
<meta charset="utf-8">
<title>Evidence Based Medicine – Trial Outcome</title>
<link rel="stylesheet" href="https://fonts.googleapis.com/css2?family=Arimo:wght@400&display=swap">
<style>
  :root {
    --bg: #eaf5fa;
    --ink: #111111;
    --red: #e02d26;
    --green: #8aae6b;
    --orange: #e57a25;
    --pill-green: #2f9e3c;
    --pill-grey: #c9c9c9;
    --pill-blue: #2a5fa8;
    --bracket: #3a3a3a;
  }
  html, body {
    margin: 0;
    padding: 0;
    overflow: hidden;
  }
  .canvas {
    position: relative;
    width: 1200px;
    height: 876px;
    background: var(--bg);
    overflow: hidden;
    font-family: "Arimo", Arial, sans-serif;
    color: var(--ink);
  }
  .figure {
    position: absolute;
    border-radius: 6px;
  }
  .figure--red { background: var(--red); }
  .figure--green { background: var(--green); }
  .figure--orange { background: var(--orange); }
  .figure--mixed-green {
    background: linear-gradient(180deg, var(--green) 0%, var(--green) 62%, var(--orange) 72%, var(--orange) 100%);
    border-radius: 40px 40px 8px 8px;
  }
  .figure--mixed-orange {
    background: linear-gradient(90deg, var(--orange) 0%, var(--orange) 70%, var(--green) 85%, var(--green) 100%);
    border-radius: 40px 40px 8px 8px;
  }
  .pill {
    position: absolute;
    border-radius: 30px;
  }
  .pill--green { background: linear-gradient(90deg, var(--pill-green) 0%, var(--pill-green) 45%, var(--pill-grey) 55%, var(--pill-grey) 100%); }
  .pill--blue { background: linear-gradient(180deg, #3a74c0 0%, var(--pill-blue) 100%); }
  .label {
    position: absolute;
    margin: 0;
    font-weight: 400;
    line-height: 1;
  }
  .label--or { left: 426px; top: 386px; font-size: 48px; }
  .label--pvalue { left: 983px; top: 394px; font-size: 52px; }
  .brackets {
    position: absolute;
    left: 0;
    top: 0;
  }
</style>
</head>
<body>
<main class="canvas">

  <!-- study population -->
  <div class="figure figure--red" style="left:162px;top:127px;width:74px;height:85px" role="img" aria-label="Two patients in red"></div>
  <div class="figure figure--green" style="left:120px;top:247px;width:157px;height:85px" role="img" aria-label="Four patients in green"></div>
  <div class="figure figure--green" style="left:100px;top:349px;width:196px;height:87px" role="img" aria-label="Five patients in green"></div>
  <div class="figure figure--orange" style="left:78px;top:475px;width:240px;height:86px" role="img" aria-label="Six patients in orange"></div>
  <div class="figure figure--orange" style="left:57px;top:572px;width:283px;height:87px" role="img" aria-label="Seven patients in orange"></div>

  <!-- treatments -->
  <div class="pill pill--green" style="left:374px;top:205px;width:171px;height:58px" role="img" aria-label="Green and grey capsule"></div>
  <p class="label label--or">OR</p>
  <div class="pill pill--blue" style="left:374px;top:565px;width:163px;height:55px" role="img" aria-label="Blue capsule"></div>

  <!-- outcome brackets -->
  <svg class="brackets" width="1200" height="876" viewBox="0 0 1200 876" aria-hidden="true">
    <g fill="none" stroke="var(--bracket)" stroke-width="2">
      <path d="M617 141 H580 V338 H617 M580 237 H617"/>
      <path d="M615 471 H579 V722 H615 M579 596 H615"/>
    </g>
  </svg>

  <!-- green capsule outcomes -->
  <div class="figure figure--green" style="left:632px;top:60px;width:74px;height:53px" role="img" aria-label="Three patients in green"></div>
  <div class="figure figure--green" style="left:632px;top:120px;width:97px;height:55px" role="img" aria-label="Four patients in green"></div>
  <div class="figure figure--orange" style="left:632px;top:209px;width:114px;height:62px" role="img" aria-label="Four patients in orange"></div>
  <div class="figure figure--red" style="left:672px;top:302px;width:30px;height:72px" role="img" aria-label="One patient in red"></div>
  <div class="figure figure--mixed-green" style="left:872px;top:97px;width:99px;height:240px" role="img" aria-label="Average patient, mostly green with orange legs"></div>

  <!-- blue capsule outcomes -->
  <div class="figure figure--green" style="left:657px;top:446px;width:46px;height:54px" role="img" aria-label="Two patients in green"></div>
  <div class="figure figure--orange" style="left:632px;top:543px;width:114px;height:62px" role="img" aria-label="Four patients in orange"></div>
  <div class="figure figure--orange" style="left:632px;top:611px;width:145px;height:63px" role="img" aria-label="Five patients in orange"></div>
  <div class="figure figure--red" style="left:676px;top:692px;width:30px;height:72px" role="img" aria-label="One patient in red"></div>
  <div class="figure figure--mixed-orange" style="left:872px;top:487px;width:97px;height:240px" role="img" aria-label="Average patient, mostly orange with a green arm"></div>

  <p class="label label--pvalue">P&gt;0.05</p>

</main>
</body>
</html>
```